Anti Cellulite Treatment Massage Oil see link https://www.shopvelarn.example/Anti-Cellulite-Treatment-Massa

i need a packaging design for Anti Cellulite Treatment Massage Oil like this
https://www.shopvelarn.example/s/ref=nb_sb_noss?url=search-alias%3Daps&field-keywords=Anti+Cellulite+Treatment+Massage+Oil+

our company is lorba see link below https://www.shopvelarn.example/Lorba-Beauty-Herbal-Extract/dp/X77QK2M4R9/ref=sr_1_1_a_it?ie=UTF8&qid=1111111111&sr=8-1&keywords=lorba

its a 8oz / 240 ml

Target Market(s)

health & beauty

Industry/Entity Type

Massage

Font styles to use
Serif
Sans Serif
Decorative
Script

Colors

Designer to choose colors to be used in the design.

Requirements
Must have
• our logo and pump like this seller
• https://www.shopvelarn.example/Anti-Cellulite-Treatment-Massage-Oil/dp/Z52HT8W3P6/ref=sr_1_1_a_it?ie=UTF8&qid=2222222222&sr=8-1&keywords=+Anti+Cellulite+Treatment+Massage+Oil
Nice to have
• the most similar to this or even better idea from this link
Should not have
• pictures on the label

```html
<!DOCTYPE html>
<html lang="en">
<head>
<meta charset="UTF-8">
<title>Lorba Anti Cellulite Massage Oil – Label</title>
<link rel="stylesheet" href="https://fonts.googleapis.com/css2?family=Arimo:wght@400;700&family=Raleway:wght@600&display=swap">
<style>
  :root {
    --bg: #ffffff;
    --gold-edge: #c4ad6c;
    --gold-mid: #e3d29e;
    --gold-light: #f1e6bf;
    --silver-dark: #9a9a9a;
    --silver-light: #e8e8e8;
    --ink: #1a1a1a;
    --band: #0d0d0d;
    --band-text: #ffffff;
  }
  * { margin: 0; padding: 0; box-sizing: border-box; }
  html, body {
    width: 1200px; height: 1200px; overflow: hidden;
    background: var(--bg);
  }
  .canvas {
    position: relative; width: 1200px; height: 1200px;
  }
  .label {
    position: absolute; left: 243px; top: 53px;
    width: 714px; height: 1094px;
    background: linear-gradient(90deg, var(--gold-edge) 0%, var(--gold-mid) 22%, var(--gold-light) 50%, var(--gold-mid) 78%, var(--gold-edge) 100%);
    font-family: "Arimo", Arial, sans-serif;
    color: var(--ink);
    text-align: center;
  }
  .label-frame {
    position: absolute; left: 27px; right: 27px; top: 40px; bottom: 40px;
    border-radius: 24px;
    border: 10px solid var(--silver-light);
    box-shadow: inset 0 0 0 2px var(--silver-dark), 0 0 0 2px var(--silver-dark);
  }
  .brand {
    position: absolute; left: 50%; top: 147px; transform: translateX(-50%);
    width: 430px; height: 90px;
    border: 4px solid var(--ink); border-radius: 45px;
    display: flex; align-items: center; justify-content: center; gap: 16px;
    font-family: "Raleway", Arial, sans-serif; font-weight: 600;
    font-size: 56px; line-height: 1; color: var(--ink);
    white-space: nowrap;
  }
  .brand-dot {
    width: 30px; height: 30px; border-radius: 50%;
    border: 5px solid var(--ink);
  }
  .brand-name { position: relative; top: -4px; }
  .product-title {
    position: absolute; left: 0; right: 0; top: 340px;
    font-weight: 700; font-size: 76px; line-height: 1;
    letter-spacing: -1px; white-space: nowrap;
  }
  .product-subtitle {
    position: absolute; left: 0; right: 0; top: 430px;
    font-weight: 400; font-size: 56px; line-height: 1;
    letter-spacing: 1px; white-space: nowrap;
  }
  .benefits {
    position: absolute; left: 62px; right: 62px; top: 575px; height: 82px;
    border: 3px solid var(--band);
    padding: 6px;
  }
  .benefits-band {
    width: 100%; height: 100%;
    background: var(--band); color: var(--band-text);
    display: flex; align-items: center; justify-content: center;
    font-size: 30px; letter-spacing: 2px; white-space: nowrap;
  }
  .description {
    position: absolute; left: 46px; right: 46px; top: 750px;
    font-size: 28px; line-height: 40px;
  }
  .description-line {
    display: block; white-space: nowrap;
    text-align: justify; text-align-last: justify;
  }
  .volume {
    position: absolute; left: 0; right: 0; top: 985px;
    font-weight: 700; font-size: 38px; line-height: 1;
  }
</style>
</head>
<body>
<main class="canvas">
  <section class="label">
    <div class="label-frame"></div>
    <div class="brand"><span class="brand-dot"></span><span class="brand-name">lorba</span></div>
    <h1 class="product-title">ANTI CELLULITE</h1>
    <h2 class="product-subtitle">MASSAGE OIL</h2>
    <div class="benefits"><div class="benefits-band">FIRMS • SMOOTHES • TONES</div></div>
    <p class="description">
      <span class="description-line">Aromatic massage oil targets stubborn</span>
      <span class="description-line">cellulite in problem are as such as hips,</span>
      <span class="description-line">thighs, buttocks and abdomen, penetrates</span>
      <span class="description-line">skin and tackles unwanted fat cells.</span>
    </p>
    <p class="volume">8 FL OZ (240 ML)</p>
  </section>
</main>
</body>
</html>
```